Tranquil Harbour Hypnotherapy 2017 DL Card Flyer

We would like a double sided DL Card Flyer design.

We are a professional Hypnotherapy Clinic looking for a fresh clean design.

Front of card is summary info and back of flyer is detailed text.

I have attached documents with text for the front (dl size hypno 1) and back (dl size hypno 2) of the card and an indicative style of layout.

There are logo files uploaded as well as one image file.

The colors we like are blue, white and yellow/gold.
Updates

please note: when using the 'new mindset new results' image, please only use the top half of the image. The girl is not to be in the image, just the words and light bulb with the chalk underline. thanks.. Added Sunday, March 19, 2017

Industry/Entity Type

Health And Wellness

Requirements
Must have
• Note. I have misspelled the www.TranquilHarbourHypnotherapy.com.au (missing an 'o' in the attachments to the brief). My error. Please amend in your design submissions.

```html
<!DOCTYPE html>
<html lang="en">
<head>
<meta charset="utf-8">
<title>Tranquil Harbour Hypnotherapy – DL Card Flyer</title>
<link href="https://fonts.googleapis.com/css2?family=Montserrat:ital,wght@0,600;0,700;0,800;1,700;1,800&family=Open+Sans:ital,wght@0,400;0,600;0,700;1,400;1,600&display=swap" rel="stylesheet">
<style>
:root{
  --navy:#1c2a6b;
  --navy-deep:#121d52;
  --blue:#24388f;
  --gold:#e3a519;
  --gold-light:#f7d35a;
  --gold-dark:#b97e0f;
  --white:#ffffff;
  --panel:#e4e4e6;
  --ink:#2a2a33;
  --backdrop:#d6d6d8;
}
*{box-sizing:border-box;margin:0;padding:0}
html,body{width:1200px;height:902px;overflow:hidden}
body{background:var(--backdrop);font-family:"Open Sans",Arial,sans-serif;position:relative}

.card{position:absolute;top:63px;width:378px;height:776px;overflow:hidden;background:linear-gradient(90deg,#e9e9ea,#ffffff 45%,#ececee);box-shadow:0 6px 18px rgba(0,0,0,.25)}
.card--front{left:163px}
.card--back{left:660px}
.card__shapes{position:absolute;inset:0;width:100%;height:100%}

/* front */
.brand{position:absolute;top:34px;left:0;right:0;display:flex;align-items:center;justify-content:center;gap:10px}
.brand__dot{width:44px;height:44px;border-radius:50%;background:var(--navy)}
.brand__name{font-family:"Montserrat",Arial,sans-serif;font-weight:700;font-size:15px;line-height:1.15;color:var(--navy);width:170px}

.chalkboard{position:absolute;left:16px;top:112px;width:318px;height:192px;border-radius:50%;background:radial-gradient(ellipse at 50% 50%,#3b3b3b,#1e1e1e 75%)}

.quote{position:absolute;top:365px;left:0;right:0;text-align:center;font-family:"Montserrat",Arial,sans-serif;font-weight:800;font-style:italic;font-size:17.5px;line-height:1.25;color:var(--white)}

.programs-title{position:absolute;top:458px;left:44px;width:302px;height:48px;display:flex;align-items:center;justify-content:center;text-align:center;font-family:"Montserrat",Arial,sans-serif;font-weight:800;font-size:13px;letter-spacing:.6px;line-height:1.35;color:var(--navy)}

.program-list{position:absolute;top:530px;left:30px;list-style:none}
.program-list li{display:flex;align-items:center;gap:10px;height:26px;font-style:italic;font-weight:600;font-size:12px;letter-spacing:-.2px;color:var(--ink)}
.program-list li::before{content:"";width:15px;height:15px;border-radius:50%;background:var(--navy);border:2px solid #b8bcd0;flex:none}

.pendulum{position:absolute;left:270px;top:512px;width:108px;height:164px;background:linear-gradient(160deg,#e8cdb8,#c9a070 55%,#8a6a45);border-radius:30px 0 0 60px;opacity:.85}

.phone-box{position:absolute;top:690px;left:34px;width:322px;height:58px;border-radius:10px;background:linear-gradient(var(--blue),var(--navy-deep));display:flex;align-items:center;justify-content:center;gap:10px}
.phone-box__number{font-family:"Montserrat",Arial,sans-serif;font-weight:800;font-size:34px;letter-spacing:.5px;color:var(--gold-light)}
.phone-icon{width:28px;height:28px}

.front-web{position:absolute;bottom:8px;left:0;right:0;display:flex;justify-content:center;align-items:center;gap:6px;font-family:"Montserrat",Arial,sans-serif;font-weight:700;font-size:9.5px;color:var(--white)}
.globe{width:11px;height:11px}

/* back */
.program{position:absolute;left:14px;width:350px;padding-bottom:8px;background:linear-gradient(90deg,var(--panel),#f4f4f5 50%,var(--panel));border-radius:8px;text-align:center}
.program__title{display:inline-block;margin-top:-12px;padding:5px 16px;border-radius:14px;background:linear-gradient(var(--gold-light),var(--gold) 55%,var(--gold-dark));border:2px solid var(--white);font-family:"Montserrat",Arial,sans-serif;font-weight:800;font-size:10.5px;color:var(--navy-deep);box-shadow:0 1px 3px rgba(0,0,0,.3)}
.program__text{margin:7px 10px 6px;text-align:justify;font-size:9.4px;line-height:1.3;color:var(--ink)}
.program__text strong{color:var(--navy);font-weight:700}
.program__text em{color:var(--navy);font-weight:600}
.program__sessions{display:inline-block;padding:3px 14px;border:1px solid var(--navy);border-radius:10px;background:var(--white);font-family:"Montserrat",Arial,sans-serif;font-weight:600;font-size:8.5px;color:var(--navy)}

.back-footer{position:absolute;bottom:18px;left:28px;right:10px;display:flex;align-items:center;gap:10px;color:var(--white)}
.back-footer__brand{display:flex;align-items:center;gap:5px;flex:none}
.back-footer__dot{width:30px;height:30px;border-radius:50%;background:var(--white)}
.back-footer__name{font-family:"Montserrat",Arial,sans-serif;font-weight:700;font-size:8.5px;line-height:1.15;width:82px}
.back-footer__contact{font-family:"Montserrat",Arial,sans-serif;font-weight:700;font-size:8px;line-height:1.6;white-space:nowrap}
.back-footer__contact .tel{font-size:12px}
.back-footer__contact span{display:flex;align-items:center;gap:5px}
</style>
</head>
<body>

<section class="card card--front">
  <svg class="card__shapes" viewBox="0 0 378 776" preserveAspectRatio="none" aria-hidden="true">
    <defs>
      <linearGradient id="band" x1="0" y1="0" x2="0" y2="1">
        <stop offset="0" stop-color="#2a3f97"/><stop offset="1" stop-color="#142060"/>
      </linearGradient>
      <linearGradient id="goldSweep" x1="0" y1="0" x2="1" y2="0">
        <stop offset="0" stop-color="#f7d35a"/><stop offset=".6" stop-color="#e3a519"/><stop offset="1" stop-color="#b97e0f"/>
      </linearGradient>
    </defs>
    <path d="M0 290 Q190 360 378 250 L378 470 Q190 520 0 470 Z" fill="url(#band)"/>
    <path d="M240 95 Q360 110 378 190 L378 240 Q365 140 240 95 Z" fill="url(#goldSweep)"/>
    <path d="M0 300 Q190 372 378 260 L378 268 Q190 380 0 310 Z" fill="url(#goldSweep)"/>
    <ellipse cx="175" cy="208" rx="166" ry="104" fill="none" stroke="#1c2a6b" stroke-width="4"/>
    <path d="M0 468 Q190 512 378 462 L378 478 Q190 530 0 484 Z" fill="url(#goldSweep)"/>
    <path d="M0 742 Q190 700 378 740 L378 776 L0 776 Z" fill="url(#band)"/>
    <path d="M30 742 Q190 716 350 742 L350 736 Q190 708 30 736 Z" fill="url(#goldSweep)"/>
  </svg>

  <div class="brand">
    <span class="brand__dot"></span>
    <span class="brand__name">Tranquil Harbour Hypnotherapy</span>
  </div>

  <div class="chalkboard" role="img" aria-label="Chalkboard illustration: 'New mindset, new result' with a glowing light bulb and chalk arrow"></div>

  <p class="quote">“THERE IS NOTHING MORE<br>IMPORTANT THAN GOOD HEALTH”</p>

  <svg class="card__shapes" viewBox="0 0 378 776" aria-hidden="true" style="pointer-events:none">
    <path d="M44 460 L346 460 L346 494 Q346 506 334 506 L56 506 Q44 506 44 494 Z" fill="url(#goldSweep)"/>
  </svg>
  <h2 class="programs-title">PROFESSIONAL<br>HYPNOSIS THERAPY PROGRAMS:</h2>

  <div class="pendulum" role="img" aria-label="Photo of a hand holding a swinging pocket watch"></div>

  <ul class="program-list">
    <li>Weight Loss (Virtual Gastric Band)</li>
    <li>Sugar Addiction</li>
    <li>Quit Smoking</li>
    <li>Chronic Fatigue &amp; Chronic Pain Relief</li>
    <li>Stress Relief &amp; Deep Relaxation</li>
  </ul>

  <div class="phone-box">
    <svg class="phone-icon" viewBox="0 0 28 28" aria-hidden="true">
      <circle cx="14" cy="14" r="12.5" fill="none" stroke="#fff" stroke-width="2"/>
      <path d="M9.5 7.5l3 3-1.6 1.8c.9 2 2.3 3.4 4.3 4.3l1.8-1.6 3 3-2 2c-5 -.6-9.9-5.5-10.5-10.5z" fill="#fff"/>
    </svg>
    <span class="phone-box__number">1300 555 017</span>
  </div>

  <p class="front-web">
    <svg class="globe" viewBox="0 0 12 12" aria-hidden="true"><circle cx="6" cy="6" r="5.2" fill="none" stroke="#fff"/><ellipse cx="6" cy="6" rx="2.3" ry="5.2" fill="none" stroke="#fff"/><path d="M1 6h10" stroke="#fff"/></svg>
    www.TranquilHarbourHypnotherapy.com.au
  </p>
</section>

<section class="card card--back">
  <svg class="card__shapes" viewBox="0 0 378 776" preserveAspectRatio="none" aria-hidden="true">
    <defs>
      <linearGradient id="bandB" x1="0" y1="0" x2="0" y2="1">
        <stop offset="0" stop-color="#2a3f97"/><stop offset="1" stop-color="#142060"/>
      </linearGradient>
      <linearGradient id="goldB" x1="0" y1="0" x2="1" y2="0">
        <stop offset="0" stop-color="#f7d35a"/><stop offset=".6" stop-color="#e3a519"/><stop offset="1" stop-color="#b97e0f"/>
      </linearGradient>
    </defs>
    <path d="M0 0 L378 0 L378 60 Q190 30 0 60 Z" fill="url(#bandB)"/>
    <path d="M0 60 Q190 30 378 60 L378 66 Q190 44 0 68 Z" fill="url(#goldB)"/>
    <path d="M0 722 Q190 690 378 722 L378 776 L0 776 Z" fill="url(#bandB)"/>
    <path d="M0 722 Q190 690 378 722 L378 716 Q190 682 0 714 Z" fill="url(#goldB)"/>
  </svg>

  <article class="program" style="top:76px">
    <h3 class="program__title">WEIGHT LOSS PROGRAM (VIRTUAL GASTRIC BAND)</h3>
    <p class="program__text">Achieve long term weight loss without dieting. Whether it’s losing 3kg or 30kg, we’ll help you become the shape and size you want to be. Our Internationally Accredited Program is proven to be 95% effective in clinical trials.</p>
    <span class="program__sessions">NUMBER OF SESSIONS: 6+</span>
  </article>

  <article class="program" style="top:196px">
    <h3 class="program__title">SUGAR ADDICTION PROGRAM</h3>
    <p class="program__text">Excess sugar intake can lead to obesity, Type 2 Diabetes and tooth decay. The habit of reaching for soft drinks, chocolate, sweets, cakes and biscuits can be hard to break. By rewiring your subconscious habits, our Program puts you back in control.</p>
    <span class="program__sessions">NUMBER OF SESSIONS: 3+</span>
  </article>

  <article class="program" style="top:321px">
    <h3 class="program__title">QUIT SMOKING PROGRAM</h3>
    <p class="program__text">The facts speak for themselves. You are 10 times more likely to quit smoking for good using hypnotherapy.<br>Expect to be a non smoker after completing the first session of our Program. <em>(12 Month Guarantee)</em></p>
    <span class="program__sessions">NUMBER OF SESSIONS: 2</span>
  </article>

  <article class="program" style="top:445px">
    <h3 class="program__title">CHRONIC FATIGUE &amp; CHRONIC PAIN RELIEF PROGRAM</h3>
    <p class="program__text">Chronic Fatigue, Fibromyalgia and Chronic Musculoskeletal Pain are diseases of modern living. The <strong>symptoms</strong> of fatigue and pain are very real, however the <strong>cause</strong> is usually emotional, and is generally hidden beyond our conscious awareness.<br>Our Program comprises Education and Hypnosis to help you regain your health, your self esteem, your friends and your life, all in a manageable timeframe.</p>
    <span class="program__sessions">NUMBER OF SESSIONS: 6+</span>
  </article>

  <article class="program" style="top:606px">
    <h3 class="program__title">STRESS RELIEF &amp; DEEP RELAXATION PROGRAM</h3>
    <p class="program__text">Our Program gently uncovers the true source of your stress, and helps you reconnect to a natural inner calm. We teach you self hypnosis so that you have the tools to continue your experience.</p>
    <span class="program__sessions">NUMBER OF SESSIONS: 3+</span>
  </article>

  <footer class="back-footer">
    <div class="back-footer__brand">
      <span class="back-footer__dot"></span>
      <span class="back-footer__name">Tranquil Harbour Hypnotherapy</span>
    </div>
    <div class="back-footer__contact">
      <span class="tel">
        <svg width="11" height="11" viewBox="0 0 12 12" aria-hidden="true"><circle cx="6" cy="6" r="5.2" fill="none" stroke="#fff"/><path d="M4 3l1.3 1.3-.7.8c.4.9 1 1.5 1.9 1.9l.8-.7L8.6 7.6l-.9.9C5.5 8.2 3.4 6.1 3.1 3.9z" fill="#fff"/></svg>
        1300 555 017
      </span>
      <span>
        <svg width="10" height="10" viewBox="0 0 12 12" aria-hidden="true"><circle cx="6" cy="6" r="5.2" fill="none" stroke="#fff"/><ellipse cx="6" cy="6" rx="2.3" ry="5.2" fill="none" stroke="#fff"/><path d="M1 6h10" stroke="#fff"/></svg>
        www.TranquilHarbourHypnotherapy.com.au
      </span>
    </div>
  </footer>
</section>

</body>
</html>
```